Clone https://brinwexo.com (fully functional wordpress site with wooCommerce)

1) Clone or recreate the site in WordPress Woocomerece
2) Connect to our existing stripe account.
3) Make our text only changes (not style changes or anything complex.

We will provide all graphics and content to be copied and pasted in place of the existing text / graphics.

Please do not submit a design only. Thanks in advance.

Target Market(s)

Wordpress developer

Number of Pages Required

5+ page

Font styles to use
Sans Serif

Colors
acd036
9bcb3c
cadf82
eaf2ce

Requirements
Must have
• Fully functional wordpress site with Woo Comerece pluged in.
Should not have
• Design only

```html
<!DOCTYPE html>
<html lang="en">
<head>
<meta charset="utf-8">
<title>Answering Services</title>
<link href="https://fonts.googleapis.com/css2?family=Roboto:wght@300;400;500;700&display=swap" rel="stylesheet">
<style>
:root{
  --green:#8dc441;
  --green-dark:#5f8f22;
  --green-soft:#cadf82;
  --green-pale:#eaf2ce;
  --ink:#222;
  --text:#555;
  --grey-bg:#f4f4f4;
  --footer:#222;
  --white:#fff;
}
*{margin:0;padding:0;box-sizing:border-box}
html,body{width:1200px;height:4018px;overflow:hidden}
body{font-family:'Roboto',sans-serif;color:var(--text);background:var(--white);position:relative}
.abs{position:absolute}
section,header,footer{position:absolute;left:0;width:1200px}

/* hero */
.hero{top:0;height:611px;overflow:hidden}
.hero-photo{position:absolute;inset:0;background:radial-gradient(ellipse at 70% 60%,#5d6166 0%,#3b3e42 45%,#1f2124 100%)}
.hero-shade{position:absolute;inset:0;background:rgba(20,22,24,.45)}
.brand-mark{left:92px;top:42px;width:40px;height:40px;border-radius:50%;background:var(--white)}
.top-phone{left:196px;top:60px;color:var(--white);font-size:15px;display:flex;align-items:center;gap:10px}
.nav{left:600px;top:62px;display:flex;font-size:14px;color:var(--white)}
.nav a{color:var(--white);text-decoration:none;margin-right:26px}
.btn{display:inline-block;font-size:11px;font-weight:500;text-transform:uppercase;text-align:center;text-decoration:none}
.btn-login{left:938px;top:58px;width:70px;height:26px;line-height:26px;background:var(--green);color:var(--white)}
.btn-trial-top{left:1021px;top:58px;width:89px;height:26px;line-height:24px;border:1px solid var(--white);color:var(--white)}
.hero-title{left:0;width:1200px;top:258px;text-align:center;color:var(--white);font-size:40px;font-weight:400;letter-spacing:.5px}
.hero-title span{color:var(--green)}
.hero-sub{left:0;width:1200px;top:320px;text-align:center;color:var(--white);font-size:15px;line-height:22px}
.btn-hero{left:513px;top:374px;width:174px;height:40px;line-height:40px;background:var(--white);color:var(--ink);font-size:12px}
.scroll-mouse{left:589px;top:546px;width:22px;height:32px;border:2px solid var(--white);border-radius:11px}
.scroll-mouse::after{content:"";position:absolute;left:8px;top:6px;width:2px;height:8px;background:var(--white)}

.section-title{left:0;width:1200px;text-align:center;font-size:32px;font-weight:400;color:var(--ink)}

/* team */
.team{top:611px;height:474px;background:var(--white)}
.member{width:300px;text-align:center;top:193px}
.avatar{width:106px;height:106px;border-radius:50%;margin:0 auto;background:linear-gradient(160deg,#d9cfc3,#8a7768);border:4px solid #eee}
.member .name{color:var(--green);font-size:14px;margin-top:22px}
.member .role{color:var(--ink);font-size:12px;margin-top:2px}
.member .quote{font-size:11px;line-height:15px;margin-top:8px;color:var(--text)}
.slider-arrow{top:278px;width:26px;height:36px;background:#eee;display:flex;align-items:center;justify-content:center}

/* features */
.features{top:1085px;height:973px;background:var(--grey-bg)}
.feature{width:260px;text-align:center}
.feature h3{font-size:13px;font-weight:500;color:var(--ink);text-transform:uppercase;margin-top:6px}
.feature p{font-size:12px;line-height:17px;margin-top:6px}
.feature svg{display:block;margin:0 auto}
.app-visual{left:420px;top:340px;width:360px;height:633px;background:linear-gradient(180deg,#e6e6e6 0%,#dcdcdc 60%,#ece6e1 100%)}
.btn-more{left:415px;top:866px;width:370px;height:40px;line-height:40px;background:var(--green);color:var(--white);font-size:11px}

/* languages */
.languages{top:2058px;height:420px}
.lang-name{font-size:44px;font-weight:700;color:var(--ink)}
.lang-hours{font-size:26px;color:var(--green);font-weight:400}
.lang-text{font-size:12px;line-height:19.5px;width:330px}
.lang-visual{left:445px;top:140px;width:300px;height:170px;background:linear-gradient(135deg,var(--green-pale),var(--green-soft))}

/* service tabs */
.service{top:2478px;height:427px}
.tabs{left:289px;top:89px;display:flex;font-size:12px;color:var(--ink)}
.tabs span{padding:0 22px;height:38px;line-height:38px}
.tabs .active{background:var(--white);border:1px solid #ddd;border-bottom:none}
.band{left:0;top:127px;width:1200px;height:300px;background:var(--green)}
.agent-photo{left:203px;top:80px;width:108px;height:108px;border-radius:50%;background:linear-gradient(160deg,#e6c7a8,#a66b45);border:4px solid var(--white)}
.agent-cap{left:157px;top:192px;width:200px;text-align:center;color:var(--white);font-size:11px;line-height:15px}
.agent-cap b{font-weight:500;font-size:12px}
.band-text{left:380px;top:188px;width:640px;color:var(--white);font-size:12px;line-height:17px}

/* stats */
.stats{top:2905px;height:311px}
.stat-num{font-size:132px;font-weight:300;color:var(--green);line-height:1}
.stat-body{width:170px}
.stat-body h4{font-size:15px;font-weight:500;color:var(--ink);text-transform:uppercase}
.stat-body p{font-size:12px;line-height:17px;margin-top:4px}

/* demo */
.demo{top:3216px;height:436px;overflow:hidden}
.demo-photo{position:absolute;inset:0;background:linear-gradient(120deg,#4b4f53,#2d3034 60%,#3c4044)}
.demo-shade{position:absolute;inset:0;background:rgba(20,22,24,.5)}
.demo h2{left:0;width:1200px;top:110px;text-align:center;color:var(--white);font-size:32px;font-weight:400}
.demo .sub{left:0;width:1200px;top:153px;text-align:center;color:var(--white);font-size:12px}
.field{height:42px;background:var(--white);font-size:11px;color:#333;padding:14px 10px;width:303px}
.btn-demo{left:289px;top:291px;width:622px;height:38px;line-height:38px;background:var(--green);color:var(--white);font-size:11px}
.chat-icon{left:1023px;top:307px;width:60px;height:60px;border-radius:50%;background:var(--green);display:flex;align-items:center;justify-content:center}
.chat-bubble{left:958px;top:380px;width:200px;padding:8px 12px;background:var(--white);font-size:11px;line-height:15px;color:var(--ink);border-radius:4px}

/* footer */
.site-footer{top:3652px;height:366px;background:var(--footer)}
.footer-art{left:147px;top:59px;width:215px;height:229px;background:#2c2e2a}
.footer-head{font-size:16px;font-weight:500;color:var(--white);text-transform:uppercase}
.footer-links{font-size:12px;color:#bbb;line-height:29.5px}
.contact-row{font-size:12px;color:#bbb;display:flex;align-items:center;gap:8px;height:30px}
.contact-row i{width:12px;height:9px;background:var(--green);display:inline-block}
.social{width:28px;height:28px;border-radius:50%;background:#3a3a3a;top:185px}
.copyright{left:0;width:1200px;top:328px;text-align:center;font-size:11px;color:#999}
</style>
</head>
<body>

<header class="hero">
  <div class="hero-photo" role="img" aria-label="Photo of a person working on a laptop beside a coffee cup"></div>
  <div class="hero-shade"></div>
  <div class="abs brand-mark" role="img" aria-label="Company mark"></div>
  <div class="abs top-phone">
    <svg width="12" height="20" viewBox="0 0 12 20"><rect x="1" y="1" width="10" height="18" rx="2" fill="none" stroke="#8dc441" stroke-width="1.6"/><circle cx="6" cy="16" r="1" fill="#8dc441"/></svg>
    (125) 555 0142
  </div>
  <nav class="abs nav"><a>Services</a><a>Customers</a><a>Pricing</a><a>Contact Us</a></nav>
  <a class="abs btn btn-login">Login</a>
  <a class="abs btn btn-trial-top">Free Trial</a>
  <h1 class="abs hero-title">WELCOME TO OUR <span>COMPANY</span></h1>
  <p class="abs hero-sub">Lorem ipsum dolor sit amet, consectetuer adipiscing elit aenean commodo<br>cum sociis natoque penatibus et magnis</p>
  <a class="abs btn btn-hero">Start a Free Trial</a>
  <div class="abs scroll-mouse"></div>
</header>

<section class="team">
  <h2 class="abs section-title" style="top:88px">HEADING 1</h2>
  <div class="abs slider-arrow" style="left:89px"><svg width="8" height="12"><path d="M7 1 2 6l5 5" stroke="#888" stroke-width="1.5" fill="none"/></svg></div>
  <div class="abs slider-arrow" style="left:1083px"><svg width="8" height="12"><path d="M1 1l5 5-5 5" stroke="#888" stroke-width="1.5" fill="none"/></svg></div>
  <div class="abs member" style="left:110px">
    <div class="avatar" role="img" aria-label="Portrait photo of a team lead"></div>
    <div class="name">John Smith</div><div class="role">Team Lead</div>
    <p class="quote">"Lorem ipsum dolor sit amet, cing elit. Aenean commodo ligula eget dolor aenean massa cum sociis."</p>
  </div>
  <div class="abs member" style="left:450px">
    <div class="avatar" role="img" aria-label="Portrait photo of a team lead"></div>
    <div class="name">John Smith</div><div class="role">Team Lead</div>
    <p class="quote">"Lorem ipsum dolor sit amet, cing elit. Aenean commodo ligula eget dolor aenean massa cum sociis."</p>
  </div>
  <div class="abs member" style="left:790px">
    <div class="avatar" role="img" aria-label="Portrait photo of a team lead"></div>
    <div class="name">John Smith</div><div class="role">Team Lead</div>
    <p class="quote">"Lorem ipsum dolor sit amet, cing elit. Aenean commodo ligula eget dolor aenean massa cum sociis."</p>
  </div>
</section>

<section class="features">
  <h2 class="abs section-title" style="top:72px">HEADING 2</h2>
  <div class="abs app-visual" role="img" aria-label="Photo of a hand holding a smartphone showing the company app"></div>

  <div class="abs feature" style="left:130px;top:168px"><svg width="36" height="36" viewBox="0 0 36 36"><path d="M24 6a13 13 0 1 0 8 20A11 11 0 0 1 24 6z" fill="none" stroke="#8dc441" stroke-width="2.4"/><path d="M12 4l1.5 3 3 .5-2.2 2 .6 3-2.9-1.5L9.1 12.5l.6-3-2.2-2 3-.5z" fill="#8dc441"/></svg><h3>Heading 1</h3><p>Lorem ipsum dolor sit amet cing elit aenean modo ligula eget dolor aenean.</p></div>
  <div class="abs feature" style="left:460px;top:168px"><svg width="36" height="36" viewBox="0 0 36 36"><path d="M24 6a13 13 0 1 0 8 20A11 11 0 0 1 24 6z" fill="none" stroke="#8dc441" stroke-width="2.4"/><path d="M12 4l1.5 3 3 .5-2.2 2 .6 3-2.9-1.5L9.1 12.5l.6-3-2.2-2 3-.5z" fill="#8dc441"/></svg><h3>Heading 2</h3><p>Lorem ipsum dolor sit amet cing elit aenean modo ligula eget dolor aenean.</p></div>
  <div class="abs feature" style="left:813px;top:168px"><svg width="36" height="36" viewBox="0 0 36 36"><path d="M24 6a13 13 0 1 0 8 20A11 11 0 0 1 24 6z" fill="none" stroke="#8dc441" stroke-width="2.4"/><path d="M12 4l1.5 3 3 .5-2.2 2 .6 3-2.9-1.5L9.1 12.5l.6-3-2.2-2 3-.5z" fill="#8dc441"/></svg><h3>Heading 3</h3><p>Lorem ipsum dolor sit amet cing elit aenean modo ligula eget dolor aenean.</p></div>

  <div class="abs feature" style="left:130px;top:352px"><svg width="36" height="36" viewBox="0 0 36 36"><path d="M24 6a13 13 0 1 0 8 20A11 11 0 0 1 24 6z" fill="none" stroke="#8dc441" stroke-width="2.4"/><path d="M12 4l1.5 3 3 .5-2.2 2 .6 3-2.9-1.5L9.1 12.5l.6-3-2.2-2 3-.5z" fill="#8dc441"/></svg><h3>Heading 4</h3><p>Lorem ipsum dolor sit amet cing elit aenean modo ligula eget dolor aenean.</p></div>
  <div class="abs feature" style="left:813px;top:352px"><svg width="36" height="36" viewBox="0 0 36 36"><path d="M24 6a13 13 0 1 0 8 20A11 11 0 0 1 24 6z" fill="none" stroke="#8dc441" stroke-width="2.4"/><path d="M12 4l1.5 3 3 .5-2.2 2 .6 3-2.9-1.5L9.1 12.5l.6-3-2.2-2 3-.5z" fill="#8dc441"/></svg><h3>Heading 5</h3><p>Lorem ipsum dolor sit amet cing elit aenean modo ligula eget dolor aenean.</p></div>

  <div class="abs feature" style="left:130px;top:534px"><svg width="36" height="36" viewBox="0 0 36 36"><path d="M24 6a13 13 0 1 0 8 20A11 11 0 0 1 24 6z" fill="none" stroke="#8dc441" stroke-width="2.4"/><path d="M12 4l1.5 3 3 .5-2.2 2 .6 3-2.9-1.5L9.1 12.5l.6-3-2.2-2 3-.5z" fill="#8dc441"/></svg><h3>Heading 6</h3><p>Lorem ipsum dolor sit amet cing elit aenean modo ligula eget dolor aenean.</p></div>
  <div class="abs feature" style="left:813px;top:534px"><svg width="36" height="36" viewBox="0 0 36 36"><path d="M24 6a13 13 0 1 0 8 20A11 11 0 0 1 24 6z" fill="none" stroke="#8dc441" stroke-width="2.4"/><path d="M12 4l1.5 3 3 .5-2.2 2 .6 3-2.9-1.5L9.1 12.5l.6-3-2.2-2 3-.5z" fill="#8dc441"/></svg><h3>Heading 7</h3><p>Lorem ipsum dolor sit amet cing elit aenean modo ligula eget dolor aenean.</p></div>

  <div class="abs feature" style="left:130px;top:724px"><svg width="36" height="36" viewBox="0 0 36 36"><path d="M24 6a13 13 0 1 0 8 20A11 11 0 0 1 24 6z" fill="none" stroke="#8dc441" stroke-width="2.4"/><path d="M12 4l1.5 3 3 .5-2.2 2 .6 3-2.9-1.5L9.1 12.5l.6-3-2.2-2 3-.5z" fill="#8dc441"/></svg><h3>Heading 8</h3><p>Lorem ipsum dolor sit amet cing elit aenean modo ligula eget dolor aenean.</p></div>
  <div class="abs feature" style="left:813px;top:724px"><svg width="36" height="36" viewBox="0 0 36 36"><path d="M24 6a13 13 0 1 0 8 20A11 11 0 0 1 24 6z" fill="none" stroke="#8dc441" stroke-width="2.4"/><path d="M12 4l1.5 3 3 .5-2.2 2 .6 3-2.9-1.5L9.1 12.5l.6-3-2.2-2 3-.5z" fill="#8dc441"/></svg><h3>Heading 9</h3><p>Lorem ipsum dolor sit amet cing elit aenean modo ligula eget dolor aenean.</p></div>

  <a class="abs btn btn-more">Learn more about our answer services</a>
</section>

<section class="languages">
  <div class="abs" style="left:86px;top:110px">
    <div class="lang-name">ENGLISH</div>
    <div class="lang-hours">24/7 Coverage</div>
    <p class="lang-text" style="margin-top:10px">Lorem ipsum dolor sit amet, consectetuer adipiscing elit. Aenean commodo ligula eget dolor aenean massa. Cum sociis natoque penatibus et magnis dis parturient montes, nascetur ridiculus mus. Donec quam felis, ultricies nec, pellentesque eu, pretium quis, sem. Nulla consequat massa quis enim donec pede justo.</p>
  </div>
  <div class="abs lang-visual" role="img" aria-label="Illustration of two speech bubbles greeting in English and Spanish"></div>
  <div class="abs" style="left:777px;top:110px">
    <div class="lang-name">SPANISH</div>
    <div class="lang-hours">7am to Midnight</div>
    <p class="lang-text" style="margin-top:10px">Lorem ipsum dolor sit amet, consectetuer adipiscing elit. Aenean commodo ligula eget dolor aenean massa. Cum sociis natoque penatibus et magnis dis parturient montes, nascetur ridiculus mus. Donec quam felis, ultricies nec, pellentesque eu, pretium quis, sem. Nulla consequat massa quis enim donec pede justo.</p>
  </div>
</section>

<section class="service">
  <h2 class="abs section-title" style="top:20px">SERVICE ON EVERY CALL</h2>
  <div class="abs tabs"><span class="active">Message Taking</span><span>Lead Collection</span><span>Appointment Scheduling</span><span>Order Processing</span></div>
  <div class="abs band">
    <div class="abs agent-photo" role="img" aria-label="Portrait photo of a live receptionist"></div>
    <div class="abs agent-cap"><b>JOHN SMITH</b><br>Live Receptionist<br>Team Member Since 2017</div>
    <svg class="abs" style="left:375px;top:40px" width="645" height="100" viewBox="0 0 645 100">
      <circle cx="18" cy="50" r="16" fill="#fff"/><path d="M13 42v16l13-8z" fill="#8dc441"/>
      <line x1="40" y1="50" x2="640" y2="50" stroke="#fff" stroke-width="2"/>
      <circle cx="48" cy="50" r="7" fill="#8dc441" stroke="#fff" stroke-width="2"/>
      <g fill="#5f8f22">
        <rect x="70" y="44" width="5" height="12"/><rect x="90" y="38" width="5" height="24"/><rect x="110" y="30" width="5" height="40"/><rect x="130" y="40" width="5" height="20"/><rect x="150" y="22" width="5" height="56"/><rect x="170" y="34" width="5" height="32"/><rect x="190" y="14" width="5" height="72"/><rect x="210" y="28" width="5" height="44"/><rect x="230" y="38" width="5" height="24"/><rect x="250" y="18" width="5" height="64"/><rect x="270" y="30" width="5" height="40"/><rect x="290" y="10" width="5" height="80"/><rect x="310" y="26" width="5" height="48"/><rect x="330" y="36" width="5" height="28"/><rect x="350" y="20" width="5" height="60"/><rect x="370" y="32" width="5" height="36"/><rect x="390" y="16" width="5" height="68"/><rect x="410" y="30" width="5" height="40"/><rect x="430" y="38" width="5" height="24"/><rect x="450" y="24" width="5" height="52"/><rect x="470" y="34" width="5" height="32"/><rect x="490" y="20" width="5" height="60"/><rect x="510" y="36" width="5" height="28"/><rect x="530" y="28" width="5" height="44"/><rect x="550" y="40" width="5" height="20"/><rect x="570" y="32" width="5" height="36"/><rect x="590" y="42" width="5" height="16"/><rect x="610" y="45" width="5" height="10"/>
      </g>
    </svg>
    <p class="abs band-text">Lorem ipsum dolor sit amet, consectetuer adipiscing elit. Aenean commodo ligula eget dolor. Aenean massa. Cum sociis natoque penatibus et magnis dis parturient montes, nascetur ridiculus mus. Donec quam felis, ultricies nec, pellentesque eu, pretium quis, sem. Nulla consequat massa quis enim. Donec pede justo, fringilla.</p>
  </div>
</section>

<section class="stats">
  <div class="abs stat-num" style="left:80px;top:100px">27</div>
  <div class="abs stat-body" style="left:228px;top:105px"><h4>Experienced</h4><p>Lorem ipsum dolor sit amet, consectetuer adipiscing elit. Aenean commodo ligula eget dolo massa.</p></div>
  <div class="abs stat-num" style="left:470px;top:100px">3</div>
  <div class="abs stat-body" style="left:549px;top:105px"><h4>Accomplished</h4><p>Lorem ipsum dolor sit amet, consectetuer adipiscing elit. Aenean commodo ligula eget dolo massa.</p></div>
  <div class="abs stat-num" style="left:795px;top:100px">24</div>
  <div class="abs stat-body" style="left:943px;top:105px"><h4>Consistent</h4><p>Lorem ipsum dolor sit amet, consectetuer adipiscing elit. Aenean commodo ligula eget dolo massa.</p></div>
</section>

<section class="demo">
  <div class="demo-photo" role="img" aria-label="Photo of a person using a smartphone at a desk"></div>
  <div class="demo-shade"></div>
  <h2 class="abs">REQUEST A DEMO</h2>
  <p class="abs sub">Lorem ipsum dolor sit amet, consectetuer adipiscing elit. Aenean commodo.</p>
  <div class="abs field" style="left:289px;top:192px">Name*</div>
  <div class="abs field" style="left:608px;top:192px">Email Address*</div>
  <div class="abs field" style="left:289px;top:243px">Phone Number*</div>
  <div class="abs field" style="left:608px;top:243px">How did you hear about Us?</div>
  <a class="abs btn btn-demo">Request a Sales Demo</a>
  <div class="abs chat-icon"><svg width="26" height="22" viewBox="0 0 26 22"><path d="M3 2h20a2 2 0 0 1 2 2v11a2 2 0 0 1-2 2H10l-6 4v-4H3a2 2 0 0 1-2-2V4a2 2 0 0 1 2-2z" fill="#fff"/></svg></div>
  <div class="abs chat-bubble">Welcome back! Do you have any questions?</div>
</section>

<footer class="site-footer">
  <div class="abs footer-art" role="img" aria-label="Illustration of a telephone surrounded by communication icons"></div>
  <div class="abs footer-head" style="left:536px;top:76px">Quick Links</div>
  <div class="abs footer-links" style="left:536px;top:103px">Services<br>Customers<br>Pricing<br>FAQ</div>
  <div class="abs footer-links" style="left:756px;top:103px">Blog<br>About<br>Careers<br>Contact Us</div>
  <div class="abs footer-head" style="left:959px;top:76px">Contact Us</div>
  <div class="abs" style="left:959px;top:102px">
    <div class="contact-row"><i></i>Sales@example.com</div>
    <div class="contact-row"><i></i>Support@example.com</div>
  </div>
  <div class="abs social" style="left:961px"></div>
  <div class="abs social" style="left:1004px"></div>
  <div class="abs social" style="left:1047px"></div>
  <div class="abs copyright">© 2017 . All rights reserved &nbsp;&nbsp; Privacy Policy &nbsp;&nbsp; Terms of Service</div>
</footer>

</body>
</html>
```